Design a WordPress website for a Wedding Company in Paradise

Seeking beautiful and creative WordPress website design for the Caribbean's leading small weddings and elopements firm. We have beautiful weddings (100+ a year), beautiful images, drone photos and videos, and much more, and we need a beautiful website to reflect that.

We like (not love) our current website, www.velmorangatherings.com. Much of the tabs and functionality can stay the same; however, we need a cleaner, crisper design that doesn't have glitches (yes, that's the responsibility of the coder in the future).

Featuring images and videos are very important. In addition, having a clean and elegant interface and aesthetic will allow the photos and imagery to shine.
Updates

Hi Designers, I'm so sorry but we haven't given this the attention it deserves, as our operations manager has been out of the office. We're pushing the deadline out a few days so that we can provide better and more detailed feedback for the submissions you've worked on, creating better results. Thank you for your patience!

Target Market(s)

Couples from the USA looking to travel to and get married in Puerto Rico, a beautiful Caribbean island.

Number of Pages Required

5+ page

Font styles to use
Other font styles liked:
• Fonts and colors are mostly provided in design guidelines. A versatile script font that's not too frilly might be useful as well.

Requirements
Must have
• -Clean and elegant web design. less is more.
-Utilize existing logo and colors
-Highlight photos and videos throughout
-Blog page design
-Video page design
-Photo gallery page design
-Landing page design for Zentro Clicklane campaigns
Should not have
• -lots of frills, hearts, palm trees, and stereotypical wedding and island imagery and themes

```html
<!DOCTYPE html>
<html lang="en">
<head>
<meta charset="utf-8">
<title>Velmoran Gatherings — Home</title>
<link href="https://fonts.googleapis.com/css2?family=Libre+Baskerville:wght@400;700&family=Open+Sans:wght@400;600&family=Poppins:wght@600&display=swap" rel="stylesheet">
<style>
:root{
  --gold:#d4a95c;
  --gold-btn:#e0c08a;
  --gold-line:#e6c790;
  --teal:#4aa99a;
  --mint:#bfe5dc;
  --ink:#222;
  --body:#666;
  --grey-box:#eeeeee;
  --badge:#ececec;
  --hero-dark:#2c2c2c;
  --white:#fff;
}
*{box-sizing:border-box;margin:0;padding:0}
html,body{width:1200px;height:3750px;overflow:hidden;background:var(--white)}
body{position:relative;font-family:"Open Sans",Arial,sans-serif;color:var(--body)}
.abs{position:absolute}
.photo{position:absolute}

/* hero */
.hero{left:0;top:0;width:1200px;height:507px;clip-path:polygon(0 0,100% 0,100% 454px,0 507px);
  background:radial-gradient(ellipse at 50% 35%,#6a6a6a 0%,#3a3a3a 35%,#1e1e1e 80%),var(--hero-dark)}
.hero-brand{left:0;width:1200px;top:30px;text-align:center;color:var(--gold);font-family:"Libre Baskerville",Georgia,serif}
.hero-brand .dot{display:inline-block;width:14px;height:14px;border-radius:50%;background:var(--teal);vertical-align:middle;margin-right:6px}
.hero-brand .name{font-size:17px;vertical-align:middle}
.hero-brand .sub{display:block;font-size:6px;letter-spacing:2px;color:var(--teal);margin-top:2px}
.hero-rule{left:0;top:83px;width:1200px;height:1px;background:rgba(255,255,255,.25)}
.nav{left:0;top:92px;width:1200px;display:flex;justify-content:center;gap:29px;font-family:"Libre Baskerville",Georgia,serif;font-size:10.5px;letter-spacing:1px;color:#eee}
.nav .on{color:var(--teal);position:relative}
.nav .on::after{content:"";position:absolute;left:50%;top:17px;width:4px;height:4px;margin-left:-2px;border-radius:50%;background:var(--teal)}
.social-vert{left:24px;top:180px;writing-mode:vertical-rl;transform:rotate(180deg);font-size:9px;letter-spacing:1px;color:var(--teal)}
.insta-link{left:36px;top:236px;font-size:9px;color:var(--teal);display:flex;align-items:center;gap:4px}
.insta-link i{display:block;width:40px;height:1px;background:var(--teal)}
.hero-bars{left:1164px;top:210px}
.hero-bars i{display:block;width:3px;height:22px;background:#fff;margin-bottom:20px}
.hero-bars i.on{background:var(--teal)}
.scroll-mark{left:588px;top:443px;width:24px;height:24px;border:1px solid rgba(255,255,255,.4);border-radius:50%}

/* section titles */
.sec-title{left:0;width:1200px;text-align:center;font-family:"Libre Baskerville",Georgia,serif;font-size:16px;letter-spacing:1px;color:var(--gold)}
.sec-title::after{content:"";display:block;width:48px;height:1px;margin:6px auto 0;background:var(--gold)}
.sec-lead{left:200px;width:800px;text-align:center;font-size:12px;line-height:20px;color:#777}

/* buttons */
.btn{position:absolute;background:var(--gold-btn);color:#3a2c10;font-family:"Libre Baskerville",Georgia,serif;font-size:10.5px;display:flex;align-items:center;justify-content:center}
.btn::after{content:"";position:absolute;left:4px;top:4px;right:-4px;bottom:-4px;border:1px solid var(--gold-line)}

/* story */
.story-head{left:163px;top:588px;width:440px;font-weight:400;font-size:16.5px;line-height:23px;letter-spacing:.6px;color:var(--teal)}
.story-text{left:163px;width:420px;font-size:10.5px;line-height:16.5px;color:#777}
.story-photo{left:606px;top:591px;width:431px;height:271px;background:linear-gradient(180deg,#cfd8dc 0%,#a8b4b3 45%,#7d6e5a 100%)}
.story-frame{left:618px;top:603px;width:407px;height:247px;border:1px solid var(--gold)}

/* gallery */
.gal-tile{top:1005px;height:375px}
.gal-caption{left:323px;top:1283px;color:#fff}
.gal-caption small{display:block;font-size:9px;letter-spacing:1px}
.gal-caption b{display:block;font-family:"Libre Baskerville",Georgia,serif;font-weight:400;font-size:12px;letter-spacing:1.5px;color:var(--gold-btn);margin-top:5px}
.gal-caption-rule{left:301px;top:1341px;width:294px;height:1px;background:rgba(224,192,138,.6)}

/* video band */
.drop-line{left:600px;top:1470px;width:1px;height:76px;background:#222}
.drop-line::after{content:"";position:absolute;left:-2px;bottom:-2px;width:5px;height:5px;border-radius:50%;background:#222}
.mint{left:0;top:1508px;width:1200px;height:277px;background:var(--mint)}
.band-title{left:0;width:1200px;top:1558px;text-align:center;font-family:"Libre Baskerville",Georgia,serif;font-weight:700;font-size:19px;color:var(--ink);letter-spacing:.5px}
.band-text{left:220px;width:760px;top:1594px;text-align:center;font-size:12px;line-height:20px;color:#333}
.video{left:300px;top:1655px;width:600px;height:293px;background:linear-gradient(180deg,#b9bcbd 0%,#8e9291 50%,#3a3630 100%)}
.video-title{left:323px;top:1758px;font-family:"Poppins",Arial,sans-serif;font-weight:600;font-size:19px;line-height:19px;color:#fff;letter-spacing:.5px}
.video-play{left:323px;top:1812px;display:flex;align-items:center;gap:10px;color:#fff;font-family:"Libre Baskerville",Georgia,serif;font-size:12px}
.video-play span{width:32px;height:32px;border:1.5px solid #fff;border-radius:50%;display:flex;align-items:center;justify-content:center}
.arrow{top:1765px;width:42px;height:42px}

/* services */
.svc-photo{width:600px;height:300px}
.svc-title{font-family:"Libre Baskerville",Georgia,serif;font-weight:400;font-size:25px;letter-spacing:1.5px;color:var(--ink)}
.svc-text{width:395px;font-size:11px;line-height:16.5px;color:#777}

/* testimonials */
.t-box{left:597px;top:2880px;width:440px;height:243px;background:var(--grey-box)}
.t-photo{left:163px;top:2913px;width:479px;height:251px;background:linear-gradient(180deg,#c8a77a 0%,#a88f5f 50%,#6f6a3e 100%)}
.t-quote{left:652px;top:2933px;width:370px;text-align:center}
.t-quote h3{font-family:"Libre Baskerville",Georgia,serif;font-weight:400;font-size:14.5px;color:var(--gold);letter-spacing:.5px}
.t-quote p{font-size:10px;line-height:15px;color:#555;margin-top:8px}
.t-quote cite{display:block;font-style:normal;font-family:"Libre Baskerville",Georgia,serif;font-size:10.5px;color:var(--gold);margin-top:15px;letter-spacing:.5px}
.pager{left:885px;top:3136px;width:152px;display:flex;align-items:center;gap:8px;font-family:"Libre Baskerville",Georgia,serif;font-style:italic;font-size:10px;color:#444}
.pager i{flex:1;height:1px;background:#bbb}

/* instagram */
.follow{left:0;width:1200px;top:3228px;text-align:center;font-size:13px;color:#333;letter-spacing:.3px}
.ig-tile{top:3267px;width:163px;height:163px}
.ig-stats{left:518px;top:3267px;width:163px;height:163px;display:flex;flex-direction:column;align-items:center;justify-content:center;gap:6px;color:#fff;font-size:11px}

/* footer */
.foot-line{left:0;top:3452px;width:1200px;height:2px;background:var(--gold-line)}
.foot-brand{left:0;width:1200px;top:3500px;text-align:center;font-family:"Libre Baskerville",Georgia,serif;color:var(--gold)}
.foot-brand .dot{display:inline-block;width:14px;height:14px;border-radius:50%;background:var(--teal);vertical-align:middle;margin-right:6px}
.foot-brand .name{font-size:17px;vertical-align:middle}
.foot-brand .sub{display:block;font-size:6px;letter-spacing:2px;color:var(--teal);margin-top:2px}
.foot-nav{left:0;width:1200px;top:3551px;display:flex;justify-content:center;gap:12px;font-family:"Libre Baskerville",Georgia,serif;font-size:10.5px;color:#333}
.foot-nav em{font-style:normal;color:#999}
.contact{top:3582px;text-align:center;font-size:9.5px;line-height:15px;color:#333}
.contact svg{display:block;margin:0 auto 6px}
.honors-label{left:287px;top:3671px;font-family:"Libre Baskerville",Georgia,serif;font-weight:700;font-size:15px;letter-spacing:1px;color:var(--ink)}
.badge{top:3657px;height:47px;border:1px solid #e3e3e3;display:flex;align-items:center;justify-content:center}
.badge i{display:block;width:70%;height:70%;background:var(--badge)}
.bottom-line{left:0;top:3714px;width:1200px;height:1px;background:#ddd}
.copy{left:163px;top:3724px;font-size:9.5px;color:#444}
.socials{left:872px;top:3720px;display:flex;gap:6px}
.socials i{display:block;width:22px;height:22px;border:1px solid var(--teal);border-radius:50%}
</style>
</head>
<body>

<!-- hero -->
<div class="abs hero" role="img" aria-label="Black and white aerial drone photograph of a couple lying on an octagonal wooden pier surrounded by dark water and clouds"></div>
<div class="abs hero-brand"><span class="dot"></span><span class="name">velmoran</span><span class="sub">GATHERINGS</span></div>
<div class="abs hero-rule"></div>
<nav class="abs nav">
  <span class="on">HOME</span><span>SERVICES</span><span>ABOUT US</span><span>GALLERY</span><span>VIDEOS</span><span>BLOG</span><span>REVIEWS</span><span>FAQS</span><span>CONTACT US</span>
</nav>
<div class="abs social-vert">YT - G+ - PI - IN - TW - FB</div>
<div class="abs insta-link"><i></i>Instagram</div>
<div class="abs hero-bars"><i></i><i class="on"></i><i></i></div>
<div class="abs scroll-mark"></div>

<!-- our story -->
<div class="abs sec-title" style="top:530px">OUR STORY</div>
<h2 class="abs story-head">EVERY WEDDING - OUTDOOR PHOTOGRAPHY - PORTRAITS - VIDEO SHOOTING - NATURAL BEAUTY.</h2>
<p class="abs story-text" style="top:647px">Velmoran Gatherings, Inc. is owned and operated by Marisol Vega, a non-denominational minister who became ordained to perform weddings, and has extensive experience planning and coordinating hundreds of weddings on our enchanted island. She will be your point of contact at every step. In her words:</p>
<p class="abs story-text" style="top:745px">Born and raised in North Carolina, the ocean has always been an important part of my life. It's what brought me to Puerto Rico five years ago. I started coming to our beautiful enchanted island in the wintertime to stand-up paddleboard, surf, kiteboard, and anything else on and around the water.</p>
<div class="btn" style="left:163px;top:834px;width:119px;height:29px">Read More Story</div>
<div class="photo story-photo" role="img" aria-label="Bride and groom embracing on a rocky beach with palm trees and the sea behind them"></div>
<div class="abs story-frame"></div>

<!-- gallery -->
<div class="abs sec-title" style="top:918px">OUR GALLERY</div>
<p class="abs sec-lead" style="top:953px">Nemo enim ipsam voluptatem quia voluptas sit aspernatur aut odit aut fugit, sed quia consequuntur magni dolores eos qui ratione voluptatem sequi nesciunt.</p>
<div class="photo gal-tile" style="left:0;width:294px;background:linear-gradient(180deg,#7b8a5a,#4f6a37 60%,#8a8478)" role="img" aria-label="Groom lifting bride in front of green hillside and old ruins"></div>
<div class="photo gal-tile" style="left:301px;width:294px;background:linear-gradient(180deg,#4a4a48,#3a3c38 60%,#2e2f2b)" role="img" aria-label="Groom kissing bride's cheek on a cloudy beach, darkened with overlay"></div>
<div class="abs gal-caption"><small>PHOTOGRAPHY</small><b>WEDDING FOR OUTDOOR</b></div>
<div class="abs gal-caption-rule"></div>
<div class="photo gal-tile" style="left:603px;width:294px;background:linear-gradient(180deg,#8a8c8a,#5a4b42 55%,#2a2626)" role="img" aria-label="Groom in dress uniform kissing bride by the sea"></div>
<div class="photo gal-tile" style="left:904px;width:296px;background:linear-gradient(180deg,#cdbfaa,#b19c86 55%,#e9e4de)" role="img" aria-label="Two brides holding a flag on rocks by the beach"></div>
<div class="btn" style="left:553px;top:1396px;width:91px;height:29px">View More</div>

<!-- video band -->
<div class="abs mint"></div>
<div class="abs drop-line"></div>
<h2 class="abs band-title">Capturing the Magic Moments</h2>
<p class="abs band-text">Lorem ipsum dolor sit amet, consectetur adipiscing elit, sed do eiusmod tempor incididunt ut labore et dolore magna aliqua. Ut enim ad minim veniam, quis nostrud exercitation ullamco laboris nisi ut aliquip ex ea commodo consequat.</p>
<div class="photo video" role="img" aria-label="Video still of a couple standing on dark rocks by crashing waves"></div>
<div class="abs video-title">Carla &amp; Jonah Elope<br>In Puerto Rico</div>
<div class="abs video-play"><span><svg width="10" height="12" viewBox="0 0 10 12"><path d="M1 1 L9 6 L1 11 Z" fill="none" stroke="#fff" stroke-width="1.2"/></svg></span>Watch video</div>
<svg class="abs arrow" style="left:235px" viewBox="0 0 42 42"><rect x="9" y="9" width="24" height="24" transform="rotate(45 21 21)" fill="none" stroke="#4aa99a"/><path d="M27 21 H15 M19 17 L15 21 L19 25" fill="none" stroke="#4aa99a" stroke-width="1.3"/></svg>
<svg class="abs arrow" style="left:922px" viewBox="0 0 42 42"><rect x="9" y="9" width="24" height="24" transform="rotate(45 21 21)" fill="none" stroke="#4aa99a"/><path d="M15 21 H27 M23 17 L27 21 L23 25" fill="none" stroke="#4aa99a" stroke-width="1.3"/></svg>
<div class="btn" style="left:539px;top:1963px;width:121px;height:29px">View More Video</div>

<!-- services -->
<div class="abs sec-title" style="top:2026px">SERVICES</div>
<p class="abs sec-lead" style="top:2062px">Nemo enim ipsam voluptatem quia voluptas sit aspernatur aut odit aut fugit, sed quia consequuntur magni dolores eos qui ratione voluptatem sequi nesciunt.</p>
<div class="photo svc-photo" style="left:0;top:2124px;background:linear-gradient(180deg,#d9a968 0%,#8d7b62 35%,#6e6355 100%)" role="img" aria-label="Couple kissing while lying in shallow water at sunset"></div>
<h3 class="abs svc-title" style="left:630px;top:2166px">ELOPEMENT PACKAGES</h3>
<p class="abs svc-text" style="left:630px;top:2223px">Bigger isn't always better. Are you traveling to Puerto Rico and want to be married? Are you starting to plan a traditional wedding at home, and it's just becoming too much? Have you already had the 'big wedding' and are looking for something entirely different this time around? Have you always dreamed of being married, simply and sweetly, with your feet in the sand?</p>
<div class="btn" style="left:630px;top:2343px;width:91px;height:29px">SEE MORE</div>
<h3 class="abs svc-title" style="left:162px;top:2470px">VOW RENEWALS</h3>
<p class="abs svc-text" style="left:162px;top:2529px">Are you taking a romantic trip to Puerto Rico for your anniversary? Would you like your family vacation to our enchanted island include a celebration of the love that brought you all together? Was your wedding a simple affair, and you're looking for more of a 'wedding experience' on a beautiful beach, with photos and perhaps video?</p>
<div class="btn" style="left:162px;top:2640px;width:91px;height:29px">SEE MORE</div>
<div class="photo svc-photo" style="left:600px;top:2424px;background:linear-gradient(90deg,#9cc3c8 0%,#b8aa98 45%,#8a6f5a 70%,#d9a4a8 100%)" role="img" aria-label="Older couple embracing on a colourful old town street, bride holding a bright bouquet"></div>
<div class="btn" style="left:539px;top:2748px;width:121px;height:29px">View More Services</div>

<!-- testimonials -->
<div class="abs sec-title" style="top:2818px">TESTIMONIALS</div>
<div class="abs t-box"></div>
<div class="photo t-photo" role="img" aria-label="Couple standing together in a field of tall golden grass"></div>
<div class="abs t-quote">
  <h3>“BEST POSSIBLE WEDDING EXPERIENCE”</h3>
  <p>“Our entire experience with Velmoran Gatherings was perfect, from the very first phone call with Marisol, to the time we parted ways after the ceremony. If you are at all nervous about the process of getting married in Puerto Rico (like we were), then worry no more. Marisol will provide you with all the information you need to know up front about getting married in Puerto Rico.”</p>
  <cite>-DANA &amp; THEO</cite>
</div>
<div class="abs pager"><i></i>01 / 05<i></i></div>

<!-- instagram -->
<svg class="abs" style="left:588px;top:3197px" width="24" height="24" viewBox="0 0 24 24" aria-hidden="true"><rect x="2" y="2" width="20" height="20" rx="6" fill="none" stroke="#222" stroke-width="2"/><circle cx="12" cy="12" r="4.5" fill="none" stroke="#222" stroke-width="2"/></svg>
<div class="abs follow">Follow by @ Velmoran Gatherings in Instagram</div>
<div class="photo ig-tile" style="left:163px;background:linear-gradient(180deg,#3f86c2,#7a5a46)" role="img" aria-label="Couple framed by a stone ruin against blue sky"></div>
<div class="photo ig-tile" style="left:341px;background:linear-gradient(180deg,#d8c7ae,#a98c6d)" role="img" aria-label="Couple kissing among pampas grass"></div>
<div class="photo ig-tile" style="left:518px;background:linear-gradient(180deg,#3a302a,#231c18)" role="img" aria-label="Smiling bride with bouquet, darkened with overlay"></div>
<div class="abs ig-stats">
  <svg width="16" height="16" viewBox="0 0 24 24"><rect x="2" y="2" width="20" height="20" rx="6" fill="none" stroke="#fff" stroke-width="2"/><circle cx="12" cy="12" r="4.5" fill="none" stroke="#fff" stroke-width="2"/></svg>
  <div>♡ 20 &nbsp;&nbsp;&nbsp; ○ 0</div>
</div>
<div class="photo ig-tile" style="left:696px;background:linear-gradient(180deg,#9bb4c4,#d9d4cc)" role="img" aria-label="Two brides holding hands on a beach path"></div>
<div class="photo ig-tile" style="left:874px;background:linear-gradient(180deg,#b4a898,#8b6e58)" role="img" aria-label="Couple kissing in soft light"></div>

<!-- footer -->
<div class="abs foot-line"></div>
<div class="abs foot-brand"><span class="dot"></span><span class="name">velmoran</span><span class="sub">GATHERINGS</span></div>
<nav class="abs foot-nav">
  <span>Home</span><em>::</em><span>Services</span><em>::</em><span>About Us</span><em>::</em><span>Gallery</span><em>::</em><span>Videos</span><em>::</em><span>Blog</span><em>::</em><span>Reviews</span><em>::</em><span>Faqs</span><em>::</em><span>Contact Us</span>
</nav>
<div class="abs contact" style="left:370px;width:160px">
  <svg width="14" height="18" viewBox="0 0 14 18"><path d="M7 1 C3.5 1 1 3.5 1 6.8 C1 11 7 17 7 17 C7 17 13 11 13 6.8 C13 3.5 10.5 1 7 1 Z" fill="none" stroke="#555"/><circle cx="7" cy="7" r="2.2" fill="none" stroke="#555"/></svg>
  845 Lorem ipsum dolor,<br>West Laborum, FL 22504.
</div>
<div class="abs contact" style="left:543px;width:100px">
  <svg width="16" height="18" viewBox="0 0 16 16"><path d="M3 1.5 L6 1.5 L7 5 L5 6.3 C6 8.5 7.5 10 9.7 11 L11 9 L14.5 10 L14.5 13 C14.5 14 13.5 14.8 12.5 14.7 C6.5 14 2 9.5 1.3 3.5 C1.2 2.5 2 1.5 3 1.5 Z" fill="none" stroke="#555"/></svg>
  555-014-2290
</div>
<div class="abs contact" style="left:655px;width:180px">
  <svg width="16" height="18" viewBox="0 0 16 12"><rect x="1" y="1" width="14" height="10" fill="none" stroke="#555"/><path d="M1 1 L8 7 L15 1" fill="none" stroke="#555"/></svg>
  hello@velmorangatherings.com
</div>
<div class="abs honors-label">OUR HONORS</div>
<div class="abs badge" style="left:446px;width:65px" role="img" aria-label="Partner badge placeholder"><i></i></div>
<div class="abs badge" style="left:542px;width:64px" role="img" aria-label="Partner badge placeholder"><i></i></div>
<div class="abs badge" style="left:636px;width:82px" role="img" aria-label="Partner badge placeholder"><i></i></div>
<div class="abs badge" style="left:729px;width:85px" role="img" aria-label="Partner badge placeholder"><i></i></div>
<div class="abs badge" style="left:824px;width:86px" role="img" aria-label="Partner badge placeholder"><i></i></div>
<div class="abs bottom-line"></div>
<div class="abs copy">© 2020, Velmoran Gatherings, Inc.</div>
<div class="abs socials"><i></i><i></i><i></i><i></i><i></i><i></i></div>

</body>
</html>
```